Tech business card design

We need an amazing business card design for our new business 'Brakka' a marketing tech startup based in Sydney, Australia. We provide an online marketplace for businesses to search and buy advertising media, connect with service providers and learn more about marketing. We wish to communicate 'cool tech', reliability and professionalism and design based around our logo.

Target Market(s)

Business Owners

Contact Information for Business Card

Name
Position
Email Address
Website
Phone Number

Font styles to use
Other font styles liked:
• Avenir & Avenir Next

Colors

Designer to choose colors to be used in the design.

```html
<!DOCTYPE html>
<html lang="en">
<head>
<meta charset="UTF-8">
<title>Brakka business card</title>
<link href="https://fonts.googleapis.com/css2?family=Mulish:wght@400;700;800&display=swap" rel="stylesheet">
<style>
  :root {
    --stage: #1f1f1f;
    --card-white: #ffffff;
    --card-black: #111111;
    --ink-navy: #1d1c3d;
    --ink-dark: #222222;
    --ink-grey: #555555;
    --band-light: #eef0f5;
  }
  * { box-sizing: border-box; margin: 0; padding: 0; }
  html, body {
    width: 1200px; height: 1000px; overflow: hidden;
    background: var(--stage);
    font-family: "Mulish", "Avenir Next", Arial, sans-serif;
  }
  .stage { position: relative; width: 1200px; height: 1000px; }
  .card {
    position: absolute; width: 580px; height: 340px;
    box-shadow: 0 18px 40px rgba(0,0,0,.55);
    overflow: hidden;
  }
  .card--front { left: 110px; top: 110px; background: var(--card-white); }
  .card--back { left: 510px; top: 540px; background: var(--card-black); }

  .wordmark { font-weight: 800; letter-spacing: -1px; line-height: 1; }
  .card--front .wordmark {
    position: absolute; left: 48px; top: 138px;
    font-size: 64px; color: var(--ink-navy);
  }
  .divider {
    position: absolute; left: 292px; top: 70px;
    width: 2px; height: 190px; background: var(--ink-navy);
  }
  .contact { position: absolute; left: 312px; top: 72px; color: var(--ink-dark); }
  .contact__name { font-weight: 700; font-size: 24px; line-height: 1.05; }
  .contact__role { font-size: 13px; color: var(--ink-grey); margin-bottom: 14px; }
  .contact__list { list-style: none; }
  .contact__item {
    display: flex; align-items: center; gap: 10px;
    font-size: 15px; margin-bottom: 10px;
  }
  .contact__icon {
    width: 24px; height: 24px; background: var(--ink-navy);
    display: flex; align-items: center; justify-content: center; flex: none;
  }

  .card--back .wordmark {
    position: absolute; left: 0; right: 0; top: 100px;
    text-align: center; font-size: 92px; color: var(--card-white);
  }
  .back-band {
    position: absolute; left: 0; right: 0; bottom: 0; height: 78px;
    background: var(--band-light);
    display: flex; align-items: center; justify-content: center;
    font-size: 17px; color: var(--ink-dark);
  }
</style>
</head>
<body>
<main class="stage">
  <section class="card card--front" aria-label="Business card front">
    <div class="wordmark">brakka</div>
    <div class="divider"></div>
    <div class="contact">
      <p class="contact__name">Marcus Lowe</p>
      <p class="contact__role">Founder, Director</p>
      <ul class="contact__list">
        <li class="contact__item">
          <span class="contact__icon">
            <svg width="14" height="14" viewBox="0 0 24 24"><path fill="#fff" d="M6.6 10.8a15 15 0 0 0 6.6 6.6l2.2-2.2c.3-.3.7-.4 1-.2 1.1.4 2.3.6 3.6.6.6 0 1 .4 1 1V20c0 .6-.4 1-1 1A17 17 0 0 1 3 4c0-.6.4-1 1-1h3.5c.6 0 1 .4 1 1 0 1.3.2 2.5.6 3.6.1.3 0 .7-.2 1z"/></svg>
          </span>+61 (0)400 555 018
        </li>
        <li class="contact__item">
          <span class="contact__icon">
            <svg width="16" height="12" viewBox="0 0 16 12"><rect x="1" y="1" width="14" height="10" fill="none" stroke="#fff" stroke-width="1.4"/><path d="M1 1l7 6 7-6" fill="none" stroke="#fff" stroke-width="1.4"/></svg>
          </span>marcus@brakkamedia.com.au
        </li>
        <li class="contact__item">
          <span class="contact__icon">
            <svg width="16" height="16" viewBox="0 0 16 16" fill="none" stroke="#fff" stroke-width="1.2"><circle cx="8" cy="8" r="6.5"/><ellipse cx="8" cy="8" rx="3" ry="6.5"/><path d="M1.5 8h13M2.5 4.5h11M2.5 11.5h11"/></svg>
          </span>www.brakkamedia.com.au
        </li>
      </ul>
    </div>
  </section>

  <section class="card card--back" aria-label="Business card back">
    <div class="wordmark">brakka</div>
    <div class="back-band">www.brakkamedia.com.au</div>
  </section>
</main>
</body>
</html>
```